Brindlewick Music Studio needs a promotional postcard design

We are looking for a postcard design for a small business that provides clients with private music lesson instruction. We are looking for a design that will convey the message of "music is fun for kids" that will appeal to parents and encourage them to sign up. We have a company logo that should be used and our color scheme is teal and turquoise. All of our contact info should be displayed as well.

Target Market(s)

Parents with young kids

Contact Information for Business Card

web: www.brindlewickmusicstudio.example
email: lessons@brindlewickmusicstudio.example
phone: 202-555-0147

Font styles to use
Serif
Sans Serif

Colors
33b8a4
86cfc6
0456a4
87cfc6

Requirements
Must have
• Music lessons in your home
• Creating little stars one at a time
• Sign Up Now
• Please use these images:
Nice to have
• Something like this sample postcard:

```html
<!DOCTYPE html>
<html lang="en">
<head>
<meta charset="utf-8">
<title>Brindlewick Music Studio – Postcard</title>
<link href="https://fonts.googleapis.com/css2?family=Marcellus&family=Jost:wght@400;500;600;700&family=Oswald:wght@500;600&display=swap" rel="stylesheet">
<style>
  :root {
    --teal: #33b8a4;
    --teal-light: #86cfc6;
    --teal-pale: #d9efec;
    --blue: #0456a4;
    --blue-deep: #034a8e;
    --white: #ffffff;
    --ink: #2b3a44;
    --page: #eef0f2;
  }
  * { margin: 0; padding: 0; box-sizing: border-box; }
  html, body { width: 870px; height: 1200px; overflow: hidden; background: var(--page); }
  .postcard {
    position: absolute; left: 13px; top: 319px;
    width: 843px; height: 562px;
    background: var(--white);
    box-shadow: 0 10px 30px rgba(0,0,0,.18);
    overflow: hidden;
    font-family: "Jost", sans-serif;
  }
  .postcard-shapes { position: absolute; inset: 0; }
  .brand {
    position: absolute; left: 104px; top: 24px;
    display: flex; align-items: center; gap: 18px;
  }
  .brand-dot { width: 78px; height: 78px; border-radius: 50%; background: var(--teal); border: 4px solid var(--teal-pale); }
  .brand-name {
    font-family: "Marcellus", serif; font-size: 30px; line-height: 1.05;
    color: var(--teal); width: 220px;
  }
  .headline { position: absolute; left: 34px; top: 140px; color: var(--white); }
  .headline-serif { font-family: "Marcellus", serif; font-size: 40px; line-height: 1; }
  .headline-sans { font-weight: 600; font-size: 34px; line-height: 1.1; letter-spacing: .5px; }
  .tagline { position: absolute; left: 32px; top: 250px; color: var(--white); }
  .tagline-small { font-size: 20px; font-weight: 500; line-height: 1; }
  .tagline-large { font-size: 36px; font-weight: 600; line-height: 1.05; }
  .phone {
    position: absolute; left: 32px; top: 340px;
    font-family: "Oswald", sans-serif; font-weight: 600; font-size: 48px; line-height: 1;
    color: var(--teal);
  }
  .email {
    position: absolute; left: 34px; top: 400px;
    display: flex; align-items: center; gap: 8px;
    font-size: 15px; color: var(--ink);
  }
  .signup {
    position: absolute; left: 30px; top: 438px; width: 262px; height: 52px;
    background: linear-gradient(var(--blue), var(--blue-deep));
    border-radius: 6px; color: var(--white);
    display: flex; align-items: center; justify-content: center; gap: 14px;
    font-size: 26px; font-weight: 700; letter-spacing: .5px;
    box-shadow: 0 3px 6px rgba(0,0,0,.2);
  }
  .signup-icon { width: 24px; height: 24px; }
  .website {
    position: absolute; left: 32px; top: 526px;
    display: flex; align-items: center; gap: 10px;
    font-size: 19px; color: var(--white);
  }
  .photo {
    position: absolute; border-radius: 50%;
  }
  .photo-main {
    left: 340px; top: 40px; width: 456px; height: 456px;
    background: radial-gradient(circle at 55% 40%, #c79a72, #7a5640 60%, #2e2a30);
  }
  .photo-small { width: 126px; height: 126px; border: 6px solid var(--white); box-shadow: 0 2px 6px rgba(0,0,0,.25); }
  .photo-1 { left: 334px; top: 381px; background: linear-gradient(135deg, #8a7a6c, #3d3f58); }
  .photo-2 { left: 444px; top: 421px; background: linear-gradient(135deg, #6b5d55, #3b4a6a); }
  .photo-3 { left: 560px; top: 421px; background: linear-gradient(135deg, #a3542a, #4a2a1c); }
  .photo-4 { left: 673px; top: 376px; background: radial-gradient(circle at 50% 40%, #4b3a36, #0e0e10); }
</style>
</head>
<body>
  <div class="postcard">
    <svg class="postcard-shapes" width="843" height="562" viewBox="0 0 843 562" aria-hidden="true">
      <defs>
        <linearGradient id="tealFill" x1="0" y1="0" x2="1" y2="1">
          <stop offset="0" stop-color="#5cc7bb"/>
          <stop offset="1" stop-color="#1f9e92"/>
        </linearGradient>
      </defs>
      <path d="M610 0 H843 V562 H520 C560 520 620 500 640 470 Z" fill="url(#tealFill)"/>
      <circle cx="720" cy="38" r="26" fill="#ffffff" opacity=".18"/>
      <circle cx="800" cy="130" r="18" fill="#ffffff" opacity=".15"/>
      <circle cx="810" cy="500" r="22" fill="#ffffff" opacity=".15"/>
      <circle cx="568" cy="268" r="256" fill="#ffffff"/>
      <circle cx="568" cy="268" r="246" fill="none" stroke="#86cfc6" stroke-width="18"/>
      <circle cx="52" cy="62" r="64" fill="none" stroke="#d9efec" stroke-width="6"/>
      <path d="M0 126 H390 L350 240 H0 Z" fill="#0456a4"/>
      <path d="M0 236 H262 A42 42 0 0 1 262 320 H0 Z" fill="#33b8a4"/>
      <path d="M0 515 H340 L380 562 H0 Z" fill="#0456a4"/>
    </svg>

    <div class="brand">
      <span class="brand-dot"></span>
      <span class="brand-name">Brindlewick Music Studio</span>
    </div>

    <div class="headline">
      <div class="headline-serif">Music Lessons</div>
      <div class="headline-sans">IN YOUR HOME</div>
    </div>

    <div class="tagline">
      <div class="tagline-small">CREATING LITTLE STARS</div>
      <div class="tagline-large">ONE AT A TIME</div>
    </div>

    <div class="phone">202-555-0147</div>

    <div class="email">
      <svg width="18" height="13" viewBox="0 0 18 13" aria-hidden="true">
        <rect x="0.5" y="0.5" width="17" height="12" fill="#33b8a4"/>
        <path d="M1 1 L9 7 L17 1" fill="none" stroke="#fff" stroke-width="1.5"/>
      </svg>
      lessons@brindlewickmusicstudio.example
    </div>

    <div class="signup">
      SIGN UP NOW
      <svg class="signup-icon" viewBox="0 0 24 24" aria-hidden="true">
        <circle cx="12" cy="12" r="11" fill="#fff"/>
        <path d="M7 7 L12 12 L7 17 Z M12 7 L17 12 L12 17 Z" fill="#0456a4"/>
      </svg>
    </div>

    <div class="website">
      <svg width="18" height="18" viewBox="0 0 18 18" aria-hidden="true" fill="none" stroke="#fff" stroke-width="1.4">
        <circle cx="9" cy="9" r="8"/>
        <ellipse cx="9" cy="9" rx="3.5" ry="8"/>
        <path d="M1 9 H17 M2.5 5 H15.5 M2.5 13 H15.5"/>
      </svg>
      www.brindlewickmusicstudio.example
    </div>

    <div class="photo photo-main" role="img" aria-label="Photo of a smiling young student making a peace sign"></div>
    <div class="photo photo-small photo-1" role="img" aria-label="Photo of a child practising violin at home"></div>
    <div class="photo photo-small photo-2" role="img" aria-label="Photo of a group of young students"></div>
    <div class="photo photo-small photo-3" role="img" aria-label="Photo of a student performing on stage"></div>
    <div class="photo photo-small photo-4" role="img" aria-label="Photo of a young violinist at a recital"></div>
  </div>
</body>
</html>
```